Funky new Serviced Apartment Company needs a website + logo

Bright Nest Serviced Accommodation is a new company aiming to attract customers who need temporary accommodation (2 days to 6 months) in city locations.

Our customers make considerable savings on longer stays compared to hotels, and have all the creature comforts of home including super-fast WIFI, comfy beds, full kitchen and modern, yet comfortable, furniture.

Another key feature of the design is a page to attract "Partners" who "Work with Us" by allowing us to manage their properties and becoming part of our network of accommodation units. I have include a brochure from one of our competitors, and a video can be found here: http://lnkvault-example.com/aptclip-7 - both can be used as I have permission.

The website design should work on all devices and screen sizes, and lend itself to a mobile app.

We would like to see website designs that are modern and simple, with a strong brand logo. The final design should communicate "Home From Home" and aim to attract professionals away from home on business for long periods of time.

Target Market(s)

Professional People working away from home for extended periods of time

Industry/Entity Type

Accommodation

Contact Information for Business Card

Name, Title, Phone Number, Email
Callum Fenwick, Owner, 07831 552907, callum.fenwick@brightnestsa-example.co.uk

Logo Text

Bright Nest Service Accommodation (Serviced Accommodation optional)

Coding

Coded - Design and coding required

Number of Pages Required

3 page

Font styles to use
Sans Serif

Requirements
Must have
• A 3 page website: Home, Partners, Contact Us
• Home page should have an area to list current apartment units, the user should be able to select a location and filter the list based on price and number of people.
• Partners page should inspire a "Work with us" call to action.
• The design should work with all screen sizes and devices.
• The design should say friendly and professional
Nice to have
• A simple logo, perhaps a smiling face made up using letters 'W' and 'H'.
• A neutral color scheme
Should not have
• No garish or vivid color scheme

```html
<!DOCTYPE html>
<html lang="en">
<head>
<meta charset="utf-8">
<title>Bright Nest Serviced Accommodation</title>
<link rel="stylesheet" href="https://fonts.googleapis.com/css2?family=Roboto:wght@400;500;700&display=swap">
<style>
:root{
  --navy:#0b2161;
  --navy-deep:#081a4f;
  --orange:#e8973e;
  --ink:#1c2a4a;
  --text:#333a48;
  --muted:#7a8294;
  --band:#edf1f8;
  --card:#f4f4f4;
  --line:#d2d7e2;
  --white:#fff;
}
*{margin:0;padding:0;box-sizing:border-box}
html,body{width:1200px;height:2946px;overflow:hidden;background:var(--white)}
body{position:relative;font-family:"Roboto",Arial,sans-serif;color:var(--text)}
.abs{position:absolute}

/* header */
.site-header{top:0;left:0;width:1200px;height:92px;background:var(--white);box-shadow:0 2px 6px rgba(0,0,0,.08);z-index:2}
.brand{left:120px;top:18px;display:flex;align-items:center;gap:14px}
.brand-dot{width:56px;height:56px;border-radius:50%;border:3px solid var(--navy)}
.brand-name{font-size:24px;font-weight:700;color:var(--navy);line-height:1.05}
.brand-name span{display:block;font-size:13px;font-weight:400;color:var(--orange);margin-top:3px}
.main-nav{top:0;left:700px;height:92px;display:flex;align-items:center}
.main-nav a{font-size:14px;color:var(--ink);text-decoration:none;padding:0 30px;text-transform:uppercase}
.main-nav a.active{color:var(--orange)}

/* hero */
.hero{top:92px;left:0;width:1200px;height:478px;background:linear-gradient(180deg,#eef0f1 0%,#d9dcdf 55%,#8d8f92 78%,#c7b49a 100%)}
.hero-title{top:465px;left:0;width:1200px;text-align:center;font-size:34px;font-weight:500;color:var(--white);text-shadow:0 2px 6px rgba(0,0,0,.45)}
.hero-arrow{top:290px}

/* search */
.search-band{top:570px;left:0;width:1200px;height:151px;background:var(--band)}
.field{top:620px;height:67px;background:var(--white);border:1px solid var(--line);padding:12px 15px}
.field label{display:block;font-size:12px;color:var(--ink)}
.field div{font-size:12px;color:var(--muted);margin-top:12px}
.search-btn{top:620px;left:945px;width:135px;height:67px;background:var(--navy);color:var(--white);border-radius:3px;display:flex;align-items:center;justify-content:center;gap:10px;font-size:17px;font-weight:500}

/* section titles */
.section-title{left:0;width:1200px;text-align:center;font-size:26px;font-weight:700;color:var(--navy);letter-spacing:.5px}
.section-title span{color:var(--orange)}

/* property cards */
.card{width:300px;height:292px;background:var(--card)}
.card-photo{position:absolute;top:0;left:0;width:300px;height:181px}
.card-meta{position:absolute;top:160px;left:0;width:300px;height:21px;background:rgba(0,0,0,.6);display:flex;justify-content:center;gap:34px;align-items:center;font-size:10px;color:var(--white);font-weight:500}
.card-meta i{display:inline-block;width:14px;height:8px;background:var(--orange);margin-right:8px;border-radius:1px;vertical-align:middle}
.card-name{position:absolute;top:198px;left:0;width:300px;text-align:center;font-size:19px;font-weight:400;color:var(--navy)}
.card-actions{position:absolute;top:242px;left:0;width:300px;display:flex;justify-content:center;gap:10px}
.price{width:96px;height:29px;background:var(--navy);color:var(--white);font-size:11px;display:flex;align-items:center;justify-content:center;border-radius:2px}
.details{width:106px;height:29px;background:var(--orange);color:var(--white);font-size:11px;display:flex;align-items:center;justify-content:center;border-radius:2px}

.pager{left:0;width:1200px;display:flex;justify-content:center;align-items:center;gap:10px}
.pager .dot{width:9px;height:9px;border-radius:50%;background:#e1e3e8}
.pager .dot.on{background:var(--navy)}

/* why choose us */
.benefit{font-size:15px;color:var(--ink)}
.benefit.right{text-align:right}

/* booking band */
.book-band{top:1915px;left:0;width:1200px;height:262px;background:linear-gradient(90deg,#1c336f 0%,#2a4585 45%,#1b3270 100%)}
.book-title{top:1968px;left:0;width:1200px;text-align:center;font-size:33px;font-weight:700;color:var(--white)}
.book-text{top:2030px;left:150px;width:900px;text-align:center;font-size:15px;line-height:24px;color:#dfe5f2}
.book-call{top:2093px;left:0;width:1200px;text-align:center;font-size:20px;font-weight:500;color:var(--white)}

/* testimonial */
.lead{left:0;width:1200px;text-align:center;font-size:14px;color:var(--text)}
.avatar{top:2318px;left:558px;width:84px;height:84px;border-radius:50%;border:3px solid var(--orange);background:radial-gradient(circle at 50% 45%,#c89a7c 0%,#9a7058 55%,#4d4a4c 100%)}
.person{top:2415px;left:0;width:1200px;text-align:center}
.person b{display:block;font-size:14px;font-weight:500;color:var(--orange);letter-spacing:.5px}
.person span{display:block;font-size:12px;color:var(--text);margin-top:3px}
.stars{display:block;font-size:11px;color:var(--orange);letter-spacing:3px;margin-top:4px}
.quote{top:2482px;left:215px;width:770px;text-align:center;font-size:13.5px;line-height:22px;color:var(--text)}

/* footer */
.site-footer{top:2633px;left:0;width:1200px;height:266px;background:var(--navy-deep)}
.f-col h4{font-size:15px;font-weight:700;color:var(--white);letter-spacing:.4px;margin-bottom:22px}
.f-col{color:var(--white);font-size:12px}
.f-links li{list-style:none;margin-bottom:20px;padding-left:12px;position:relative}
.f-links li::before{content:"";position:absolute;left:0;top:6px;width:3px;height:3px;background:var(--white);border-radius:50%}
.contact-line{display:flex;align-items:center;gap:10px;margin-top:12px}
.newsletter input{display:block;width:224px;height:30px;border:0;padding:0 8px;font:12px "Roboto",sans-serif;margin-top:14px}
.submit{display:inline-block;margin-top:14px;background:var(--orange);color:var(--white);font-weight:700;font-size:13px;padding:8px 10px}
.social{display:flex;align-items:center;gap:12px;margin-bottom:11px;font-size:12px}
.social i{width:28px;height:28px;border-radius:50%;display:inline-block}
.copyright{top:2899px;left:0;width:1200px;height:47px;background:var(--orange);color:var(--white);font-size:12px;display:flex;align-items:center;justify-content:center;letter-spacing:.3px}
</style>
</head>
<body>

<header class="site-header abs">
  <div class="brand abs">
    <div class="brand-dot"></div>
    <div class="brand-name">BRIGHT NEST<span>Serviced Accommodation</span></div>
  </div>
  <nav class="main-nav abs">
    <a class="active" href="#">Home</a>
    <a href="#">Partners</a>
    <a href="#">Contact Us</a>
  </nav>
</header>

<div class="hero abs" role="img" aria-label="Bright modern open-plan living room with grey sofa, kitchen and large windows"></div>
<svg class="hero-arrow abs" style="left:48px" width="40" height="76" viewBox="0 0 40 76"><path d="M36 4 L6 38 L36 72" fill="none" stroke="#fff" stroke-width="3"/></svg>
<svg class="hero-arrow abs" style="left:1112px" width="40" height="76" viewBox="0 0 40 76"><path d="M4 4 L34 38 L4 72" fill="none" stroke="#fff" stroke-width="3"/></svg>
<h1 class="hero-title abs">Home Away From Home</h1>

<section class="search-band abs"></section>
<div class="field abs" style="left:120px;width:288px"><label>Where</label><div>Anywhere</div></div>
<div class="field abs" style="left:424px;width:244px"><label>When</label><div>Anytime</div></div>
<div class="field abs" style="left:684px;width:244px"><label>Guests</label><div>1 guest &#8964;</div></div>
<div class="search-btn abs">
  <svg width="18" height="18" viewBox="0 0 18 18"><circle cx="7.5" cy="7.5" r="5.5" fill="none" stroke="#fff" stroke-width="2.2"/><path d="M11.5 11.5 L16.5 16.5" stroke="#fff" stroke-width="2.4" stroke-linecap="round"/></svg>
  Search
</div>

<h2 class="section-title abs" style="top:766px">PROPERTY <span>LISTING</span></h2>

<article class="card abs" style="left:120px;top:840px">
  <div class="card-photo" role="img" aria-label="Modern apartment living room with city view" style="background:linear-gradient(135deg,#dfe5ea,#8d9198 60%,#2e2f33)"></div>
  <div class="card-meta"><span><i></i>02</span><span><i></i>04</span><span><i></i>yes</span></div>
  <h3 class="card-name">Morden Apartment</h3>
  <div class="card-actions"><span class="price">180 (USD)</span><span class="details">More Details</span></div>
</article>
<article class="card abs" style="left:450px;top:840px">
  <div class="card-photo" role="img" aria-label="Villa lounge with wall-mounted television and wooden console" style="background:linear-gradient(180deg,#e4e2de,#bcb5ab 60%,#6e5140)"></div>
  <div class="card-meta"><span><i></i>02</span><span><i></i>04</span><span><i></i>yes</span></div>
  <h3 class="card-name">Masons de Villa</h3>
  <div class="card-actions"><span class="price">180 (USD)</span><span class="details">More Details</span></div>
</article>
<article class="card abs" style="left:780px;top:840px">
  <div class="card-photo" role="img" aria-label="Dark duplex living area with bookshelves and sofa" style="background:linear-gradient(135deg,#3b3e47,#232631 55%,#7a6b66)"></div>
  <div class="card-meta"><span><i></i>02</span><span><i></i>04</span><span><i></i>yes</span></div>
  <h3 class="card-name">Luxurious Deplux</h3>
  <div class="card-actions"><span class="price">180 (USD)</span><span class="details">More Details</span></div>
</article>
<article class="card abs" style="left:120px;top:1168px">
  <div class="card-photo" role="img" aria-label="White modern kitchen with island" style="background:linear-gradient(135deg,#f3f4f5,#d8dbde 60%,#9da3a8)"></div>
  <div class="card-meta"><span><i></i>02</span><span><i></i>04</span><span><i></i>yes</span></div>
  <h3 class="card-name">Masons Villas</h3>
  <div class="card-actions"><span class="price">180 (USD)</span><span class="details">More Details</span></div>
</article>
<article class="card abs" style="left:450px;top:1168px">
  <div class="card-photo" role="img" aria-label="Open dining room with white chairs and kitchen" style="background:linear-gradient(160deg,#e9e6de,#c6c0b2 55%,#8c8a6a)"></div>
  <div class="card-meta"><span><i></i>02</span><span><i></i>04</span><span><i></i>yes</span></div>
  <h3 class="card-name">Masons de Villa</h3>
  <div class="card-actions"><span class="price">180 (USD)</span><span class="details">More Details</span></div>
</article>
<article class="card abs" style="left:780px;top:1168px">
  <div class="card-photo" role="img" aria-label="Compact apartment kitchen and lounge with warm lighting" style="background:linear-gradient(135deg,#ebe7e1,#bfb3a5 55%,#6b4f3e)"></div>
  <div class="card-meta"><span><i></i>02</span><span><i></i>04</span><span><i></i>yes</span></div>
  <h3 class="card-name">Luxurious Deplux</h3>
  <div class="card-actions"><span class="price">180 (USD)</span><span class="details">More Details</span></div>
</article>

<div class="pager abs" style="top:1494px">
  <svg width="16" height="26" viewBox="0 0 16 26"><path d="M13 2 L3 13 L13 24" fill="none" stroke="#9aa0ad" stroke-width="2"/></svg>
  <span class="dot on"></span><span class="dot"></span><span class="dot"></span><span class="dot"></span>
  <svg width="16" height="26" viewBox="0 0 16 26"><path d="M3 2 L13 13 L3 24" fill="none" stroke="#9aa0ad" stroke-width="2"/></svg>
</div>

<h2 class="section-title abs" style="top:1570px">WHY <span>CHOOSE US</span></h2>

<svg class="abs" style="top:1620px;left:0" width="1200" height="295" viewBox="0 1620 1200 295">
  <path d="M430 1915 A170 170 0 0 1 770 1915" fill="none" stroke="#9a9a9a" stroke-width="9"/>
  <g stroke="#0b2161" stroke-width="1.5">
    <line x1="542" y1="1733" x2="548" y2="1762"/>
    <line x1="660" y1="1733" x2="652" y2="1762"/>
    <line x1="733" y1="1773" x2="712" y2="1794"/>
    <line x1="779" y1="1848" x2="750" y2="1850"/>
    <line x1="469" y1="1773" x2="490" y2="1794"/>
    <line x1="425" y1="1848" x2="453" y2="1858"/>
  </g>
  <g fill="#fff" stroke="#0b2161" stroke-width="2">
    <circle cx="548" cy="1765" r="5"/><circle cx="652" cy="1765" r="5"/>
    <circle cx="712" cy="1798" r="5"/><circle cx="750" cy="1855" r="5"/>
    <circle cx="490" cy="1798" r="5"/><circle cx="453" cy="1862" r="5" stroke="#e8973e"/>
  </g>
  <circle cx="600" cy="1858" r="52" fill="#fff" stroke="#0b2161" stroke-width="3"/>
  <g fill="#fff" stroke="#0b2161" stroke-width="2.5">
    <circle cx="542" cy="1691" r="41"/>
    <circle cx="660" cy="1691" r="41"/>
    <circle cx="762" cy="1744" r="41"/>
    <circle cx="821" cy="1848" r="41"/>
    <circle cx="440" cy="1744" r="41"/>
  </g>
  <circle cx="383" cy="1848" r="42" fill="#e8973e"/>
  <g fill="#0b2161"><rect x="522" y="1690" width="40" height="5"/><rect x="528" y="1695" width="3" height="14"/><rect x="553" y="1695" width="3" height="14"/><circle cx="532" cy="1679" r="5"/><circle cx="552" cy="1679" r="5"/></g>
  <circle cx="660" cy="1684" r="14" fill="#0b2161"/><text x="660" y="1690" font-family="Roboto,sans-serif" font-size="17" font-weight="700" fill="#fff" text-anchor="middle">$</text>
  <path d="M640 1706 h40" stroke="#0b2161" stroke-width="4" stroke-linecap="round"/>
  <g stroke="#0b2161" stroke-width="3" stroke-linecap="round"><line x1="744" y1="1734" x2="780" y2="1734"/><line x1="744" y1="1754" x2="780" y2="1754"/></g>
  <circle cx="754" cy="1734" r="5" fill="#0b2161"/><circle cx="772" cy="1754" r="5" fill="#0b2161"/>
  <circle cx="821" cy="1848" r="18" fill="none" stroke="#0b2161" stroke-width="3"/>
  <path d="M812 1849 l6 6 l12 -13" fill="none" stroke="#0b2161" stroke-width="3.5" stroke-linecap="round" stroke-linejoin="round"/>
  <rect x="426" y="1726" width="28" height="36" rx="3" fill="none" stroke="#0b2161" stroke-width="3"/>
  <g stroke="#0b2161" stroke-width="3"><line x1="432" y1="1738" x2="448" y2="1738"/><line x1="432" y1="1746" x2="448" y2="1746"/><line x1="432" y1="1754" x2="442" y2="1754"/></g>
  <rect x="367" y="1832" width="32" height="30" rx="3" fill="none" stroke="#fff" stroke-width="3"/>
  <line x1="367" y1="1840" x2="399" y2="1840" stroke="#fff" stroke-width="3"/>
  <g fill="#fff"><rect x="372" y="1845" width="5" height="4"/><rect x="380" y="1845" width="5" height="4"/><rect x="388" y="1845" width="5" height="4"/><rect x="372" y="1852" width="5" height="4"/><rect x="380" y="1852" width="5" height="4"/></g>
</svg>
<div class="benefit right abs" style="top:1655px;left:190px;width:300px">Expert Support From The Start</div>
<div class="benefit abs" style="top:1655px;left:718px">Maximise Your Income</div>
<div class="benefit right abs" style="top:1734px;left:85px;width:300px">Managing Your Bookings</div>
<div class="benefit abs" style="top:1734px;left:822px">You'll Be In Control</div>
<div class="benefit right abs" style="top:1827px;left:30px;width:300px;line-height:23px">Regular Bookings, Regular<br>Payments</div>
<div class="benefit abs" style="top:1830px;left:879px">Your Peace of Mind</div>

<section class="book-band abs" role="img" aria-label="Modern apartment building at dusk under a navy overlay"></section>
<h2 class="book-title abs">BOOK YOUR APARTMENT</h2>
<p class="book-text abs">Lorem ipsum dolor sit amet, consectetur adipisicing elit. Doloribus, ex illum corporis quibusdam numquam quisquam optio explicabo. Officiis odit quia odio dignissimos eius repellat id!</p>
<p class="book-call abs">call us on : +(00)555-0142-318</p>

<h2 class="section-title abs" style="top:2222px">HAPPY <span>CUSTOMERS</span></h2>
<p class="lead abs" style="top:2278px">Lorem ipsum dolor sit amet, consectetur adipiscing elit. Aliquam nec viverra erat Aenean elit tellus.</p>
<div class="avatar abs" role="img" aria-label="Portrait photo of the customer"></div>
<div class="person abs"><b>REID ASHWORTH</b><span>( Harborline Capital )</span><span class="stars">★★★★★</span></div>
<p class="quote abs">Lorem ipsum dolor sit amet, consectetuer adipiscing elit, sed diam nonummy nibh tempor cum soluta nobis consectetuer adipiscing. Lorem ipsum dolor sit amet, consectetur adipiscing elit. Nulla convallis egestas rhoncus. Donec facilisis fermentum sem, ac viverra ante luctus vel.</p>
<div class="pager abs" style="top:2572px"><span class="dot"></span><span class="dot on"></span><span class="dot"></span></div>

<footer class="site-footer abs">
  <div class="f-col abs" style="left:163px;top:40px">
    <h4>QUICK LINKS</h4>
    <ul class="f-links"><li>Home</li><li>Partners</li><li>Contact Us</li></ul>
  </div>
  <div class="f-col abs" style="left:342px;top:40px">
    <h4>CONTACT DETAILS</h4>
    <div style="font-weight:700">Bright Nest Serviced Accommodation</div>
    <div style="margin-top:4px;line-height:17px">42 Alder Row Suite 7<br>Ipsum, NY 12345</div>
    <div class="contact-line"><svg width="12" height="12" viewBox="0 0 12 12"><path d="M2 1 h3 l1 3 l-2 1 a7 7 0 0 0 3 3 l1-2 l3 1 v3 a1 1 0 0 1-1 1 A10 10 0 0 1 1 2 a1 1 0 0 1 1-1z" fill="#e8973e"/></svg>555 014 2207</div>
    <div class="contact-line"><svg width="12" height="12" viewBox="0 0 12 12"><rect x="1" y="4" width="10" height="6" fill="#e8973e"/><rect x="3" y="1" width="6" height="3" fill="#e8973e"/></svg>555 014 2207</div>
    <div class="contact-line"><svg width="12" height="10" viewBox="0 0 12 10"><rect x="0" y="1" width="12" height="8" fill="#e8973e"/><path d="M0 1 l6 5 l6-5" fill="none" stroke="#081a4f" stroke-width="1"/></svg>inquiry@brightnest-example.com</div>
  </div>
  <div class="f-col newsletter abs" style="left:646px;top:40px">
    <h4>NEWSLETTER SIGNUP</h4>
    <div style="width:230px;line-height:17px">Lorem ipsum dolor sit amet, consectet adipiscing elit erat non.</div>
    <input type="text" value="Enter Your Email">
    <span class="submit">SUBMIT →</span>
  </div>
  <div class="f-col abs" style="left:926px;top:40px">
    <h4>FOLLOW US</h4>
    <div class="social"><i style="background:#3b5a98"></i>FRIENDLINE</div>
    <div class="social"><i style="background:#3aa3dd"></i>CHIRPFEED</div>
    <div class="social"><i style="background:#d44c3c"></i>SEARCHPLUS</div>
    <div class="social"><i style="background:#2f80b8"></i>WORKLINK</div>
  </div>
</footer>
<div class="copyright abs">COPYRIGHT © 2017 BRIGHT NEST SERVICED ACCOMMODATION. ALL RIGHTS RESERVED.</div>

</body>
</html>
```